Stationery Design Project

see attached logo and business card layout, envelopes, letterhead, proposal, and invoice stationery needs to all flow.

Industry/Entity Type

Business

```html
<!DOCTYPE html>
<html lang="en">
<head>
<meta charset="utf-8">
<title>Granite Road Works Letterhead</title>
<link href="https://fonts.googleapis.com/css2?family=Cormorant+Garamond:wght@500&display=swap" rel="stylesheet">
<style>
  :root {
    --ink: #111111;
    --band: #000000;
    --paper: #ffffff;
    --mark-grey: #8c8c8c;
    --mark-gold: #fddd96;
  }
  html, body {
    margin: 0;
    padding: 0;
    overflow: hidden;
    background: var(--paper);
  }
  .letterhead {
    position: relative;
    width: 927px;
    height: 1200px;
    overflow: hidden;
    background: var(--paper);
  }
  .side-band {
    position: absolute;
    left: 0;
    top: 0;
    width: 71px;
    height: 100%;
    background: var(--band);
  }
  .brand {
    position: absolute;
    left: 128px;
    top: 96px;
    color: var(--ink);
    font-family: "Cormorant Garamond", serif;
    font-weight: 500;
  }
  .brand-name {
    margin: 0;
    font-size: 30px;
    line-height: 1;
    font-weight: 500;
  }
  .brand-tagline {
    margin: 6px 0 0;
    font-size: 14px;
    line-height: 1;
  }
  .brand-watermark {
    position: absolute;
    left: 71px;
    top: 790px;
    width: 760px;
    height: 410px;
    border-radius: 60% 40% 0 0 / 55% 45% 0 0;
    background: linear-gradient(160deg, var(--mark-grey) 0%, var(--mark-grey) 38%, var(--mark-gold) 62%, var(--mark-gold) 100%);
    opacity: 0.35;
  }
  .footer-info {
    position: absolute;
    left: 400px;
    width: 468px;
    top: 1096px;
    margin: 0;
    text-align: center;
    font-family: "Cormorant Garamond", serif;
    font-weight: 500;
    font-size: 18.5px;
    line-height: 22px;
    color: var(--ink);
  }
</style>
</head>
<body>
  <main class="letterhead">
    <div class="side-band"></div>

    <header class="brand">
      <h1 class="brand-name">Granite Road Works</h1>
      <p class="brand-tagline">Built Right, Built to Last</p>
    </header>

    <div class="brand-watermark" role="img" aria-label="Large faint brand decoration in grey and pale gold"></div>

    <p class="footer-info">
      Lorem ipsum dolor sit amet Consectetur adipiscing elit.<br>
      Nam eget ante mollis libero Rutrum tincidunt et quis est.<br>
      Suspendisse 0987654321
    </p>
  </main>
</body>
</html>
```